Crust Harbor Hotel Coupon

Would like to design a coupon that is for hotels' staff and to be dropped off at the hotel front office anytime someone calls from a hotel and as a Thank You for hotel staff for recommending us. Coupon value to be $ 2.00. Should say Thank You or Thank you for recommending us. Need our phone number 250 614 3750 on it. Color scheme to be Green and Red as in the attached logo. Coupon to be designed for printing size 3.5 inches high and 7.5 inches wide. Rear should say Fastest Delivery, Favourite Pizza for Sports teams etc. Ask for group deals. Attached logo to be on the coupon. Coupon should say coupon # and space left for us write number

```html
<!DOCTYPE html>
<html lang="en">
<head>
<meta charset="utf-8">
<title>Crust Harbor Coupon – Rear</title>
<link rel="stylesheet" href="https://fonts.googleapis.com/css2?family=Inter:wght@600;700&display=swap">
<style>
  :root {
    --paper: #f1f2f1;
    --glow: #a9d9bb;
    --glow-soft: #d6ebdd;
    --red: #ad1a1e;
    --red-deep: #5c1012;
    --black-red: #150b0b;
    --ink: #111111;
    --white: #ffffff;
  }
  html, body {
    margin: 0;
    padding: 0;
    overflow: hidden;
    background: var(--paper);
  }
  .coupon-rear {
    position: relative;
    width: 1200px;
    height: 560px;
    overflow: hidden;
    font-family: "Inter", Arial, sans-serif;
    background:
      radial-gradient(circle at 600px 267px,
        var(--glow) 0px,
        var(--glow) 330px,
        var(--glow-soft) 390px,
        var(--paper) 470px);
  }
  .hero-disc {
    position: absolute;
    left: 273px;
    top: -60px;
    width: 654px;
    height: 654px;
    border-radius: 50%;
    background: linear-gradient(45deg,
      var(--black-red) 12%,
      var(--red-deep) 50%,
      var(--red) 88%);
  }
  .tagline {
    position: absolute;
    left: 80px;
    top: 80px;
    margin: 0;
    font-size: 22px;
    font-weight: 700;
    line-height: 1.2;
    color: var(--ink);
  }
  .group-deals {
    position: absolute;
    right: 80px;
    top: 80px;
    margin: 0;
    font-size: 22px;
    font-weight: 600;
    color: var(--ink);
  }
  .call-line {
    position: absolute;
    left: 0;
    width: 1200px;
    top: 266px;
    margin: 0;
    text-align: center;
    font-size: 24px;
    font-weight: 600;
    color: var(--white);
  }
</style>
</head>
<body>
  <main class="coupon-rear">
    <div class="hero-disc"></div>
    <p class="tagline">Fastest Delivery,<br>Favourite Pizza<br>for Sports teams.</p>
    <p class="group-deals">Ask for group deals!</p>
    <p class="call-line">Call us: 250 614 3750</p>
  </main>
</body>
</html>
```